Yacht, Boats, Watersports company needs a redesign of business card

Hello Designers!
We are a Boat dealership company that sells fun in the water, we sell boats, Yachts, Kayaks and also yacht WaterSport toys. We are looking to redesign our business cards in to something a little bit more sophisticated. in a way that we can make better use of our company colors. I'm attaching a zipped file containing the company 3 sets of company logo which one is an horizontal another one is a vertical and also a chromed 3d logo. Also is included two set of business cards that we use and also some designs that i think it's interesting. We use PMS 2026c Orange and PMS 7687C Blue. I would like to see at least two different options with the orange as accent and also using blue as an accent color. It's really important for the business cards to have a font option and size that is legible to most people. Our current website is wwww.corvellamarine.com. Please visit if you want to have a better feeling of the Boat dealership
You can send Single sided or double side options. We are now using single sided but we may be open for a double side option if we really like the design.
Target Market(s)
Marine, boat sales, yacht sales, water toys sales/
Contact Information for Business Card
Name: Dale Pritchett
Address: 718 West Halden Lane,
Dania Beach, FL 33019
Phone: 954-382-7146
Fax: 954:382-7139
Cell: 954-451-8320
Email: 212@corvellamarine.com
Website: corvellamarine.com
Requirements
Must have
- the current information of the business card provided.
logo
use the PMS Colors
Nice to have
- a touch of elegance and sophistication but simple
Should not have
- should not have any typography that is hard to read, the card should be simple but yet sophisticated.

```html
<!DOCTYPE html>
<html lang="en">
<head>
<meta charset="utf-8">
<title>Corvella Marine — Business Card</title>
<link rel="stylesheet" href="https://fonts.googleapis.com/css2?family=Didact+Gothic&family=Poppins:wght@600&display=swap">
<style>
  :root {
    --backdrop: #123e6f;
    --brand-orange: #c2603a;
    --brand-blue: #163a6b;
    --card-white: #ffffff;
    --ring-on-orange: rgba(255, 255, 255, 0.18);
    --ring-on-white: rgba(194, 96, 58, 0.2);
  }
  * { margin: 0; padding: 0; box-sizing: border-box; }
  html, body {
    width: 1200px;
    height: 900px;
    overflow: hidden;
    background: var(--backdrop);
  }
  .business-card {
    position: absolute;
    left: 295px;
    top: 258px;
    width: 609px;
    height: 385px;
    background: var(--card-white);
    overflow: hidden;
  }
  .accent-panel {
    position: absolute;
    left: 0;
    top: 0;
    width: 225px;
    height: 100%;
    background: var(--brand-orange);
  }
  .decor-ring {
    position: absolute;
    left: 0;
    top: 0;
    width: 609px;
    height: 385px;
  }
  .brand {
    position: absolute;
    left: 269px;
    top: 39px;
    display: flex;
    align-items: center;
    gap: 9px;
  }
  .brand-mark {
    width: 40px;
    height: 40px;
    border: 3px solid var(--brand-blue);
    border-radius: 50%;
  }
  .brand-name {
    font-family: "Poppins", sans-serif;
    font-weight: 600;
    font-size: 12px;
    letter-spacing: 0.6px;
    text-transform: uppercase;
    color: var(--brand-blue);
  }
  .person-name {
    position: absolute;
    left: 269px;
    top: 120px;
    font-family: "Poppins", sans-serif;
    font-weight: 600;
    font-size: 31px;
    line-height: 1.3;
    color: var(--brand-blue);
  }
  .contact {
    position: absolute;
    left: 270px;
    font-family: "Didact Gothic", sans-serif;
    font-size: 14.5px;
    line-height: 17.4px;
    letter-spacing: 1.4px;
    color: var(--brand-blue);
  }
  .contact-address { top: 206px; }
  .contact-lines { top: 250px; }
</style>
</head>
<body>
  <section class="business-card">
    <div class="accent-panel"></div>
    <svg class="decor-ring" viewBox="0 0 609 385" aria-hidden="true">
      <defs>
        <clipPath id="panel-clip"><rect x="0" y="0" width="225" height="385"/></clipPath>
        <clipPath id="white-clip"><rect x="225" y="0" width="384" height="385"/></clipPath>
      </defs>
      <circle cx="189" cy="192" r="144" fill="none" stroke="var(--ring-on-orange)" stroke-width="27" clip-path="url(#panel-clip)"/>
      <circle cx="189" cy="192" r="144" fill="none" stroke="var(--ring-on-white)" stroke-width="27" clip-path="url(#white-clip)"/>
    </svg>

    <div class="brand">
      <span class="brand-mark"></span>
      <span class="brand-name">Corvella Marine</span>
    </div>

    <h1 class="person-name">Dale Pritchett</h1>

    <p class="contact contact-address">718 West Halden Lane, Dania<br>Beach, FL 33019</p>

    <p class="contact contact-lines">
      TEL: 954-382-7146<br>
      FAX: 954:382-7139<br>
      Cell: 954-451-8320<br>
      Email: 212@corvellamarine.com<br>
      URL: corvellamarine.com
    </p>
  </section>
</body>
</html>
```